Redesign of business card for Birchline Mechanical

We are looking for a new design for our business cards for Birchline Mechanical. We are a plumbing & HVAC construction company, operating on the West Coast of Canada and USA. Logo attached.
Industry/Entity Type
Construction - Plumbing & HVAC
Contact Information for Business Card
Name, address, phone numbers, email, website address
Look and feel
Each slider illustrates characteristics of the customer's brand and the style your logo design should communicate.

```html
<!DOCTYPE html>
<html lang="en">
<head>
<meta charset="utf-8">
<title>Birchline Mechanical — Business Card</title>
<link rel="stylesheet" href="https://fonts.googleapis.com/css2?family=Montserrat:wght@400;500;700&display=swap">
<style>
  :root {
    --backdrop: #e9e4dc;
    --card-white: #ffffff;
    --ink: #231f20;
    --ink-soft: #2b2b2b;
    --band-dark: #2a2a2a;
    --band-grey: #6b6b6b;
    --card-black: #0f0f0f;
    --pattern-light: #6a6a6a;
    --pattern-dark: #141414;
    --on-dark: #ffffff;
  }
  * { margin: 0; padding: 0; box-sizing: border-box; }
  html, body { width: 900px; height: 1200px; overflow: hidden; }
  body {
    position: relative;
    background: var(--backdrop);
    font-family: "Montserrat", Arial, sans-serif;
    color: var(--ink);
  }
  .card {
    position: absolute;
    width: 742px;
    height: 440px;
    border-radius: 22px;
    overflow: hidden;
  }
  /* Front */
  .card-front { left: 80px; top: 131px; background: var(--card-white); }
  .brand-name {
    position: absolute;
    left: 110px; top: 196px;
    width: 230px;
    text-align: center;
    font-weight: 700;
    font-size: 27px;
    line-height: 1.2;
    color: var(--ink);
  }
  .divider {
    position: absolute;
    left: 356px; top: 156px;
    width: 2px; height: 146px;
    background: var(--ink);
  }
  .person-name {
    position: absolute;
    left: 375px; top: 152px;
    font-weight: 700; font-size: 24px;
    color: var(--ink);
  }
  .person-title {
    position: absolute;
    left: 375px; top: 184px;
    font-weight: 500; font-size: 15px;
    color: var(--ink-soft);
  }
  .contact-list {
    position: absolute;
    left: 374px; top: 221px;
    list-style: none;
  }
  .contact-item {
    display: flex; align-items: center;
    height: 30px;
    font-size: 15.5px; font-weight: 500;
    color: var(--ink-soft);
  }
  .contact-icon { width: 16px; height: 16px; margin-right: 11px; fill: var(--ink); flex: none; }
  .address-band { position: absolute; left: 0; top: 371px; width: 742px; height: 35px; }
  .address-text {
    position: absolute;
    left: 0; top: 371px; width: 545px; height: 35px;
    display: flex; align-items: center; justify-content: flex-end;
    padding-right: 42px;
    font-size: 15.5px; color: var(--on-dark);
  }
  /* Back */
  .card-back { left: 78px; top: 638px; background: var(--card-black); }
  .back-pattern {
    position: absolute; inset: 0;
    background: linear-gradient(115deg, var(--pattern-light) 0%, var(--pattern-dark) 45%, var(--card-black) 100%);
  }
  .back-brand {
    position: absolute;
    left: 508px; top: 310px;
    width: 150px;
    text-align: center;
    font-weight: 700; font-size: 15px; line-height: 1.25;
    color: var(--on-dark);
  }
</style>
</head>
<body>

<section class="card card-front" aria-label="Business card front">
  <div class="brand-name">Birchline<br>Mechanical</div>
  <div class="divider"></div>
  <h1 class="person-name">Daniel Reyes</h1>
  <p class="person-title">Managing Director</p>
  <ul class="contact-list">
    <li class="contact-item">
      <svg class="contact-icon" viewBox="0 0 24 24" aria-hidden="true"><path d="M6.6 10.8c1.4 2.8 3.8 5.1 6.6 6.6l2.2-2.2c.3-.3.7-.4 1-.2 1.1.4 2.3.6 3.6.6.6 0 1 .4 1 1V20c0 .6-.4 1-1 1C10.6 21 3 13.4 3 4c0-.6.4-1 1-1h3.5c.6 0 1 .4 1 1 0 1.3.2 2.5.6 3.6.1.3 0 .7-.2 1L6.6 10.8z"/></svg>
      888.555.0142
    </li>
    <li class="contact-item">
      <svg class="contact-icon" viewBox="0 0 24 24" aria-hidden="true"><path d="M3 5h18c.6 0 1 .4 1 1v.4l-10 7-10-7V6c0-.6.4-1 1-1zm-1 3.7l10 7 10-7V18c0 .6-.4 1-1 1H3c-.6 0-1-.4-1-1V8.7z"/></svg>
      info@birchlinemechanical.com
    </li>
    <li class="contact-item">
      <svg class="contact-icon" viewBox="0 0 24 24" aria-hidden="true"><circle cx="12" cy="12" r="9" fill="none" stroke="#231f20" stroke-width="2"/><ellipse cx="12" cy="12" rx="4" ry="9" fill="none" stroke="#231f20" stroke-width="2"/><path d="M3 12h18" stroke="#231f20" stroke-width="2"/></svg>
      www.birchlinemechanical.com
    </li>
  </ul>
  <svg class="address-band" viewBox="0 0 742 35" aria-hidden="true">
    <polygon points="0,0 545,0 527,35 0,35" fill="var(--band-dark)"/>
    <polygon points="555,0 742,0 742,35 537,35" fill="var(--band-grey)"/>
  </svg>
  <p class="address-text">48 Cedar Cove Road Tidewell, WA 98400</p>
</section>

<section class="card card-back" aria-label="Business card back">
  <div class="back-pattern" role="img" aria-label="Repeating glossy brand-mark pattern across the black card"></div>
  <div class="back-brand">Birchline<br>Mechanical</div>
</section>

</body>
</html>
```